New corporate e-mail signature

We need a new e-mail signature for our company that is clean and professional. The requests are attached in a document.

Target Market(s)

CFO, CTO, Controllers, leaders, decision-makers.

Industry/Entity Type

Information Technology

Colors

Designer to choose colors to be used in the design.

Requirements
Must have
• See the PowerPoint document.
• - keep it as simple as possible.
• - same style as our new website design
• - It has to look good in all e-mail readers, and on all surfaces.
Nice to have
• - Please also attach 'best practise' for how to use the signature.
Should not have
• See the PowerPoint document. Use our color palette.
• - Do not include photo!

```html
<!DOCTYPE html>
<html lang="en">
<head>
<meta charset="utf-8">
<title>Email Signature – Daniel Whitmore</title>
<link rel="stylesheet" href="https://fonts.googleapis.com/css2?family=Montserrat:wght@500;600;700&display=swap">
<style>
  :root {
    --page-bg: #ffffff;
    --brand-teal: #1a7f99;
    --brand-teal-light: #3aa3b8;
    --brand-navy: #1e3a4f;
    --text-dark: #1f2a33;
    --divider: #2b5a70;
    --shadow: rgba(0, 0, 0, 0.16);
  }
  * { box-sizing: border-box; margin: 0; padding: 0; }
  html, body {
    width: 1200px;
    height: 817px;
    overflow: hidden;
    background: var(--page-bg);
    font-family: "Montserrat", sans-serif;
  }
  .canvas {
    position: relative;
    width: 1200px;
    height: 817px;
  }
  .signature {
    position: absolute;
    left: 127px;
    top: 270px;
    width: 945px;
    height: 270px;
  }
  .signature__top {
    position: absolute;
    left: 0; top: 0;
    width: 945px;
    height: 168px;
  }
  .person {
    position: absolute;
    left: 81px;
    top: 44px;
  }
  .person__name {
    font-size: 31px;
    font-weight: 700;
    color: var(--brand-teal);
    letter-spacing: 0.2px;
  }
  .person__role {
    margin-top: 12px;
    font-size: 21px;
    font-weight: 600;
    color: var(--text-dark);
  }
  .signature__divider {
    position: absolute;
    left: 444px;
    top: 6px;
    width: 2px;
    height: 144px;
    background: var(--divider);
  }
  .contact {
    position: absolute;
    left: 555px;
    top: 38px;
    list-style: none;
  }
  .contact__item {
    display: flex;
    align-items: center;
    gap: 14px;
    height: 24px;
    margin-bottom: 26px;
    font-size: 19px;
    font-weight: 600;
    color: var(--brand-teal);
  }
  .contact__icon { width: 18px; height: 18px; flex: none; }
  .signature__band {
    position: absolute;
    left: 0;
    top: 168px;
    width: 945px;
    height: 21px;
    background: linear-gradient(90deg, var(--brand-teal) 0%, var(--brand-teal-light) 45%, var(--brand-navy) 75%, var(--brand-teal) 100%);
  }
  .signature__footer {
    position: absolute;
    left: 45px;
    top: 189px;
    width: 855px;
    height: 60px;
    background: var(--page-bg);
    box-shadow: 0 18px 22px -12px var(--shadow);
  }
  .brand {
    position: absolute;
    left: 54px;
    top: 16px;
    font-size: 27px;
    font-weight: 700;
    color: var(--brand-teal);
  }
  .website {
    position: absolute;
    left: 327px;
    top: 20px;
    font-size: 17px;
    font-weight: 600;
    color: var(--brand-teal);
  }
  .social {
    position: absolute;
    left: 640px;
    top: 20px;
    display: flex;
    gap: 52px;
    list-style: none;
  }
  .social__dot {
    width: 22px;
    height: 22px;
    border-radius: 50%;
    background: var(--brand-navy);
  }
</style>
</head>
<body>
<main class="canvas">
  <section class="signature" aria-label="Email signature">
    <div class="signature__top">
      <div class="person">
        <p class="person__name">Daniel Whitmore</p>
        <p class="person__role">Business Analyst</p>
      </div>
      <div class="signature__divider"></div>
      <ul class="contact">
        <li class="contact__item">
          <svg class="contact__icon" viewBox="0 0 18 18" aria-hidden="true">
            <rect x="2" y="4" width="14" height="10" rx="1" fill="none" stroke="var(--brand-navy)" stroke-width="1.8"/>
            <path d="M2.5 4.5 L9 10 L15.5 4.5" fill="none" stroke="var(--brand-navy)" stroke-width="1.8"/>
          </svg>
          <span>mail@northgrid.com</span>
        </li>
        <li class="contact__item">
          <svg class="contact__icon" viewBox="0 0 18 18" aria-hidden="true">
            <path d="M5 2.5 L7.5 6 L6 7.8 C7 10 8.2 11.2 10.2 12 L12 10.5 L15.5 13 L14 15.5 C8 15.5 2.5 10 2.5 4 Z" fill="var(--brand-navy)"/>
          </svg>
          <span>001 234 567 890</span>
        </li>
      </ul>
    </div>
    <div class="signature__band" role="img" aria-label="Teal brand band with fine diagonal line pattern"></div>
    <div class="signature__footer">
      <p class="brand">Northgrid</p>
      <p class="website">www.northgrid.com</p>
      <ul class="social" aria-label="Social profiles">
        <li class="social__dot"></li>
        <li class="social__dot"></li>
        <li class="social__dot"></li>
      </ul>
    </div>
  </section>
</main>
</body>
</html>
```